Flyer for 1 day Lean Manufacturing event

I have: 2 sample flyers for the same event, a Word document with the text I would like to use, photos to include. Not all photos need to be included.

I would like a 2 (maybe 1?) page flyer I can use for marketing this and future events. Can be MS Publisher format, or other as preferred - please provide PDF also just in case.

```html
<!DOCTYPE html>
<html lang="en">
<head>
<meta charset="utf-8">
<title>One Day Lean Manufacturing Simulation – Flyer</title>
<link rel="stylesheet" href="https://fonts.googleapis.com/css2?family=Bebas+Neue&family=Oswald:wght@400;500;600&family=Montserrat:wght@400;600;700;900&display=swap">
<style>
:root{
  --backdrop:#ddd0ad;
  --paper:#ecebe9;
  --paper-white:#f6f6f5;
  --navy:#1e3f8f;
  --red:#c3222b;
  --red-deep:#9e1a22;
  --orange:#e0762a;
  --yellow:#f5c518;
  --ink:#2b2b2b;
  --grey:#b9b9b9;
}
*{box-sizing:border-box;margin:0;padding:0}
html,body{width:1200px;height:835px;overflow:hidden;background:var(--backdrop)}
body{position:relative;font-family:'Montserrat',sans-serif;color:var(--ink)}
.page{position:absolute;top:93px;width:459px;height:649px;background:var(--paper-white);overflow:hidden}
.page--front{left:88px}
.page--back{left:642px;background:var(--paper)}
.layer{position:absolute;left:0;top:0}
.abs{position:absolute}

/* front */
.brand-mark{left:40px;top:56px;display:flex;align-items:center;gap:8px;font-weight:900;font-size:17px;color:var(--navy)}
.brand-mark .square{width:22px;height:22px;background:var(--red)}
.event-title{left:199px;top:27px;font-family:'Bebas Neue',sans-serif;font-weight:400;font-size:41px;line-height:35px;color:var(--navy);letter-spacing:.3px}
.powered{left:200px;top:138px;font-weight:700;font-size:11.5px;color:var(--orange)}
.headline{left:39px;top:186px;font-weight:900;color:#fff;font-size:29px;line-height:24px}
.headline .bang{display:block;font-size:48px;line-height:46px;color:var(--yellow)}
.intro{left:43px;top:278px;width:200px;color:#fff;font-weight:600;font-size:8.6px;line-height:10.6px}
.price{left:280px;top:206px;width:72px;height:72px;border-radius:50%;background:radial-gradient(circle at 40% 35%,#ee8a3c,var(--orange));color:#fff;text-align:center;font-family:'Oswald',sans-serif;box-shadow:2px 3px 6px rgba(0,0,0,.25)}
.price .lbl{display:block;margin-top:9px;font-size:8px;line-height:9px}
.price .amt{display:block;font-size:19px;line-height:20px}
.price .sub{display:block;font-size:7.5px;line-height:8px}
.details{right:33px;font-family:'Oswald',sans-serif;text-align:right;color:var(--ink)}
.date{top:222px;font-size:11.5px;line-height:15px;font-weight:500}
.time{top:261px;font-size:11.5px;font-weight:500}
.venue{top:285px;font-size:7.6px;line-height:10.5px}
.icon{position:absolute;right:10px;width:14px;height:14px}
.catering{left:313px;top:320px;width:112px;height:24px;border-radius:5px;background:var(--orange);color:#fff;font-family:'Oswald',sans-serif;font-size:9px;display:flex;align-items:center;justify-content:center}
.photo-frame{background:#fff;padding:7px;box-shadow:1px 1px 4px rgba(0,0,0,.15)}
.photo{width:100%;height:100%;background:linear-gradient(160deg,#c9ccd0,#8e8b84 55%,#5a6270)}
.front-photo{left:40px;top:349px;width:205px;height:262px}
.body-copy{left:264px;top:357px;width:174px;font-size:7.4px;line-height:10.6px;text-align:justify;color:#333}
.turn-bar{left:0;top:627px;width:445px;height:7px;background:var(--grey)}
.turn-label{right:9px;top:627px;font-size:5px;font-weight:700}

/* back */
.covered{left:23px;top:45px;font-family:'Bebas Neue',sans-serif;font-weight:400;color:var(--navy)}
.covered .l1{display:block;font-size:27px;line-height:24px}
.covered .l2{display:block;font-size:48px;line-height:40px;color:var(--red-deep)}
.covered .l2 small{font-size:27px;color:var(--navy)}
.covered .l3{display:block;font-size:27px;line-height:24px}
.back-photo{left:276px;top:36px;width:160px;height:136px;padding:5px;background:#d4d4d4}
.takeaways{left:23px;top:144px;width:413px;list-style:none;font-size:7.2px;line-height:11.8px;color:#333;text-align:justify}
.takeaways li{position:relative}
.takeaways li::before{content:"";position:absolute;left:-11px;top:5px;width:2.5px;height:2.5px;background:var(--red);border-radius:50%}
.takeaways b{font-weight:700;color:#111}
.tab{left:56px;top:433px;width:21px;height:79px;background:#fff}
.portrait{left:80px;top:433px;width:133px;height:148px}
.bio{left:218px;top:433px;width:218px;color:#fff;font-weight:700;font-size:6.9px;line-height:9.9px;text-align:justify;border-top:1.5px solid #fff;border-bottom:1.5px solid #fff;padding:6px 0 8px}
.contact{right:22px;top:601px;text-align:right;color:#fff;font-family:'Oswald',sans-serif;font-size:6.6px;line-height:9px}
</style>
</head>
<body>

<section class="page page--front">
  <svg class="layer" width="459" height="649" viewBox="0 0 459 649" aria-hidden="true">
    <path d="M0 190 Q120 140 459 175 L459 649 L0 649 Z" fill="#e2e2e2"/>
    <path d="M10 215 Q120 160 410 184 L300 330 Q255 345 225 352 Q60 420 40 640 L0 640 L0 215 Z" fill="var(--red)"/>
    <path d="M10 215 Q120 160 410 184 L370 230 Q200 190 10 260 Z" fill="#d03038" opacity=".6"/>
    <path d="M0 640 L0 250 Q20 420 60 640 Z" fill="#dadada"/>
    <path d="M36 300 Q20 350 38 398" fill="none" stroke="var(--yellow)" stroke-width="4" stroke-linecap="round"/>
    <path d="M28 392 L42 404 L46 386 Z" fill="var(--yellow)"/>
  </svg>

  <div class="abs brand-mark"><span class="square"></span>Lean Forge</div>
  <h1 class="abs event-title">One Day Lean<br>Manufacturing<br>Simulation</h1>
  <p class="abs powered">Powered by Lean Forge</p>

  <h2 class="abs headline">Start the<br>Year with a<span class="bang">BANG!</span></h2>
  <p class="abs intro">Our one day Lean and TOC Simulation shows you how to integrate Lean into your process, and demonstrates how you can lead or support successful implementation.</p>

  <div class="abs price"><span class="lbl">COST:</span><span class="amt">$350</span><span class="sub">PER PERSON<br>INCL GST</span></div>

  <p class="abs details date">FRIDAY 16TH<br>FEBRUARY 2024</p>
  <svg class="icon" style="top:226px" viewBox="0 0 14 14" aria-hidden="true"><rect x="1" y="2.5" width="12" height="10.5" rx="1.5" fill="none" stroke="var(--red)" stroke-width="1.4"/><rect x="1" y="2.5" width="12" height="3" fill="var(--red)"/><rect x="3.5" y="0.5" width="1.4" height="3" fill="var(--red)"/><rect x="9" y="0.5" width="1.4" height="3" fill="var(--red)"/></svg>
  <p class="abs details time">8AM-5PM</p>
  <svg class="icon" style="top:261px" viewBox="0 0 14 14" aria-hidden="true"><circle cx="7" cy="7" r="6.3" fill="var(--red)"/><path d="M7 3.5 V7 L9.5 8.5" stroke="#fff" stroke-width="1.3" fill="none"/></svg>
  <p class="abs details venue">HARBOURVIEW HOTEL, PARKSIDE ROOM<br>12 MERIDIAN WAY NORTHGATE HEIGHTS<br>QLD 4999</p>
  <svg class="icon" style="top:287px" viewBox="0 0 14 14" aria-hidden="true"><path d="M7 13 C3 8.5 2.5 6.8 2.5 5.3 A4.5 4.5 0 0 1 11.5 5.3 C11.5 6.8 11 8.5 7 13 Z" fill="var(--red)"/><circle cx="7" cy="5.2" r="1.7" fill="#fff"/></svg>

  <div class="abs catering">CATERING PROVIDED</div>

  <div class="abs photo-frame front-photo"><div class="photo" role="img" aria-label="Photo of workshop participants building products at a table during the simulation"></div></div>

  <p class="abs body-copy">The Simulation uses Lean manufacturing principles to work towards perfecting manufacturing processes. An analysis of the material and information flow leads to the elimination of non-value adding activities, elevating a "typical" production environment to best practice. The immersive nature of the Simulation results in a much deeper and long lasting understanding of the principles of Lean. These principles work in companies regardless of size or sector.<br>The Simulation recreates the manufacturing environment through the hands-on assembly of "products" at separate work stations and all participants work together to refine the process and achieve optimum output. (Challenge: try to beat the standing record)<br>By applying best practice techniques under practical conditions, participants will accelerate awareness and understanding that will enhance the success rate and effectiveness of your Lean program.</p>

  <div class="abs turn-bar"></div>
  <p class="abs turn-label">PLEASE TURN OVER</p>
</section>

<section class="page page--back">
  <svg class="layer" width="459" height="649" viewBox="0 0 459 649" aria-hidden="true">
    <path d="M0 0 H459 V398 Q220 350 0 385 Z" fill="#e9e9e8"/>
    <path d="M14 392 Q200 398 459 410 L459 649 L40 649 Q10 520 14 392 Z" fill="var(--red)"/>
    <path d="M0 385 Q2 520 40 649 L0 649 Z" fill="#dcdcdc"/>
  </svg>

  <h2 class="abs covered"><span class="l1">What will be</span><span class="l2">Covered<small>and</small></span><span class="l3">What you will take away</span></h2>

  <div class="abs back-photo"><div class="photo" role="img" aria-label="Photo of a group working around long tables in a training room"></div></div>

  <ul class="abs takeaways">
    <li>How to rate your company using a <b>Manufacturing</b></li>
    <li style="margin-top:3px"><b>Excellence model</b>, and use the model to drive improvement.</li>
    <li>How to maximise productivity using the <b>Theory of Constraints</b>.</li>
    <li>The application of lean methodologies across manufacturing, financials, administration and the supply chain.</li>
    <li>Ability to <b>develop people</b> into a cohesive, flexible, and empowered autonomous team to achieve a common goal of improved performance.</li>
    <li>Ability to list, discuss and review process issues by using basic <b>problem solving techniques</b></li>
    <li>How to identify and <b>eliminate non-value added</b> activities.</li>
    <li>How to distinguish between push and <b>pull systems</b> and understand the control method of <b>Kanban</b> pull signals to balance supply and demand, improve lead times and reduce work-in progress.</li>
    <li>Understand why, when, and how to practice <b>set up time reduction</b>.</li>
    <li>Why large <b>batch sizes</b> are not cost effective and increase inventory, lead times, and reduce flexibility.</li>
    <li>Why consistent processes give quality results through <b>standard work</b> practices and procedures.</li>
    <li>The importance of <b>visual performance measures</b> in driving behaviours.</li>
    <li>How the implementation of <b>5S housekeeping</b> is the cornerstone of best practice.</li>
    <li>The importance of quality at source and <b>mistake proofing</b>.</li>
    <li>Why <b>preventative and autonomous maintenance</b> is critical to overall equipment effectiveness.</li>
    <li>Understand the key best practices areas of: <b>Leading and Managing Change, Teamwork, Set-up Reduction, Process and Material Flow, Focused Improvement, 5S, and Visual Performance Measures</b>.</li>
  </ul>

  <div class="abs tab"></div>
  <div class="abs photo-frame portrait"><div class="photo" style="background:linear-gradient(160deg,#cfcfcb,#9a9a95)" role="img" aria-label="Portrait photo of the presenter"></div></div>

  <p class="abs bio">Daniel Harrow is a skilled consultant, specialising in maximising profit, capacity and unlocking production efficiency.<br>He is a professional engineer with 18 years of consulting experience in production system design, continuous improvement tools and rapid interventions.<br>Prior to entering consulting he gained wide-ranging experience in the Australian automotive industry implementing Lean and other World Class practices across the supply chain including Parts and Accessory, Tier 1 Supply, and Vehicle Assembly Plant. He is also a specialist in Inventory Optimisation, Energy Optimisation, Excel Auditing, and the Supply Chain Operations Reference (SCOR) Model</p>

  <p class="abs contact">For more information contact: Paul Renner, Skills<br>Development and Training Officer<br>M: 0400 555 218 &nbsp;E: paul.renner@skillsoffice.example.org</p>
</section>

</body>
</html>
```